Poster Design Project

We are launching a new company Q Vizo, we sell advertising on digital signage and we are launching our company selling ads at our 2 locations, Barlow Heights Sports and Rec Club and the Merrowby Bay Sports and Rec Club. We want to advertise that we have 5 10 and 15 ad slots available and ads start from as little as $27.00 per week. We need to let people know we offer 10% discount to KNBTA members. it needs to have the following contact details to get more information, Marcus 0427359012 and marcus@qvizo.com.au. As a new launch we are offering for the first 10 customers one of 2 discounts, get 4 weeks free all you have to pay is the content creation fee ($99 for 5 second ad) or 4 weeks free and free content creation if you sign up to a 18 week contract.

Update: need the add to start wit something like this but you can be creative:

Need to get you message or brand out, Have you heard of digital sinage?
We have ads avaliable starting from $27 per week at one of our locations.

Or something like that, as i am introducing my company they dont know what i do you untill they read this poster.

Target Market(s)

Targeting small to medium buisness

Industry/Entity Type

Advertising

Requirements
Must have
• Logo

```html
<!DOCTYPE html>
<html lang="en">
<head>
<meta charset="utf-8">
<title>Q Vizo – Digital Signage Advertising</title>
<link rel="stylesheet" href="https://fonts.googleapis.com/css2?family=Nunito:wght@700;800;900&display=swap">
<style>
  :root {
    --green-dark: #1e760f;
    --green-mid: #2a8f1a;
    --green-text: #23901a;
    --price-red: #d8140f;
    --offer-orange: #f0911c;
    --contact-blue: #1d5a9e;
    --ink: #111111;
    --paper: #ffffff;
  }
  html, body {
    margin: 0;
    padding: 0;
    width: 1200px;
    height: 1000px;
    overflow: hidden;
    background: var(--paper);
  }
  body { font-family: "Nunito", Arial, sans-serif; }
  .poster {
    position: relative;
    width: 1200px;
    height: 1000px;
    background: var(--paper);
  }
  .header-shape {
    position: absolute;
    left: 0;
    top: 0;
  }
  .text { position: absolute; margin: 0; white-space: nowrap; font-weight: 800; }
  .intro { left: 275px; top: 40px; font-size: 31px; color: var(--paper); }
  .new { left: 503px; top: 68px; font-size: 84px; font-weight: 900; color: var(--paper); line-height: 1; }
  .signage { left: 636px; top: 148px; font-size: 32px; color: var(--paper); }
  .price {
    position: absolute;
    left: 800px;
    top: 40px;
    width: 170px;
    transform: rotate(45deg);
    transform-origin: center;
    color: var(--price-red);
    text-align: center;
    line-height: 1;
    font-weight: 900;
  }
  .price-amount { display: block; font-size: 36px; }
  .price-unit { display: block; font-size: 34px; }
  .price-unit small { font-size: 18px; margin-right: 4px; }
  .advertise { left: 0; width: 1214px; top: 248px; text-align: center; font-size: 54px; font-weight: 900; color: var(--green-text); }
  .brand {
    position: absolute;
    left: 472px;
    top: 372px;
    display: flex;
    align-items: center;
    gap: 22px;
  }
  .brand-mark { width: 96px; height: 96px; background: var(--green-mid); }
  .brand-name { font-size: 72px; font-weight: 900; color: var(--ink); line-height: 1; }
  .member-discount {
    left: 930px;
    top: 455px;
    font-size: 25px;
    color: var(--offer-orange);
    transform: rotate(90deg);
    transform-origin: 0 0;
    left: 946px;
  }
  .section-title { left: 263px; font-size: 25px; color: var(--green-text); }
  .section-offer { top: 494px; }
  .section-places { top: 687px; }
  .rule { position: absolute; left: 258px; }
  .rule-offer { top: 531px; }
  .rule-places { top: 723px; }
  .details {
    position: absolute;
    left: 300px;
    width: 618px;
    margin: 0;
    text-align: center;
    font-size: 18.5px;
    font-weight: 800;
    color: var(--ink);
    line-height: 25px;
  }
  .details-offer { top: 550px; }
  .details-places { top: 745px; }
  .contact {
    position: absolute;
    left: 283px;
    top: 864px;
    margin: 0;
    font-size: 27px;
    font-weight: 800;
    color: var(--contact-blue);
    line-height: 35px;
    font-style: normal;
  }
</style>
</head>
<body>
<main class="poster">
  <svg class="header-shape" width="1200" height="1000" viewBox="0 0 1200 1000" aria-hidden="true">
    <defs>
      <linearGradient id="header-fade" x1="0" y1="0" x2="0" y2="1">
        <stop offset="0" stop-color="#1c740d"/>
        <stop offset="0.3" stop-color="#5a9e4c"/>
        <stop offset="0.65" stop-color="#a6cf98"/>
        <stop offset="1" stop-color="#f6fbf3"/>
      </linearGradient>
      <linearGradient id="rule-fade" x1="0" y1="0" x2="1" y2="0">
        <stop offset="0" stop-color="#2a9a17"/>
        <stop offset="0.55" stop-color="#8cc878"/>
        <stop offset="1" stop-color="#ffffff"/>
      </linearGradient>
    </defs>
    <polygon points="258,8 752,8 952,205 952,335 872,472 330,472 258,345" fill="url(#header-fade)"/>
    <rect x="258" y="531" width="585" height="10" fill="url(#rule-fade)"/>
    <rect x="258" y="723" width="585" height="10" fill="url(#rule-fade)"/>
  </svg>

  <p class="text intro">Your AD will be in a</p>
  <p class="text new">NEW</p>
  <p class="text signage">Digital Signage</p>

  <p class="price"><span class="price-amount">$27.00</span><span class="price-unit"><small>per</small>week</span></p>

  <h1 class="text advertise">Advertise with</h1>
  <div class="brand">
    <span class="brand-mark"></span>
    <span class="brand-name">Q Vizo</span>
  </div>

  <p class="text member-discount">10% discount for KNBTA members</p>

  <h2 class="text section-title section-offer">Special offer for first 10 customers</h2>
  <p class="details details-offer">Get 4 weeks free all you have to pay is the<br>content creation fee ($99 for 5 second ad)<br>or<br>4 weeks free and free content creation if you sign up to a 18<br>week contract</p>

  <h2 class="text section-title section-places">Available Ads Places</h2>
  <p class="details details-places">Barlow Heights Sports and Rec Club - 5 10 ad slots<br>The Merrowby Bay Sports and Rec Club - 15 ad slots</p>

  <address class="contact">Contact Q Vizo,<br>Marcus - 0427359012<br>marcus@qvizo.com.au</address>
</main>
</body>
</html>
```